KeyHarbor needs a modern business card

We are a modern conveyancing company and we need to appeal to the top (Multi-million dollar properties)and bottom on the property conveyancing market but our sweet spot is the middle of the market. I like professional with a hint of unconventional.

Target Market(s)

As above

Industry/Entity Type

Real Estate

Contact Information for Business Card

Back Of card:
thinking black with the logo and a tag line (I could be wrong about the black)
Tag line - Careful Advice, Dependable Results

Front of Card:
Marissa Toll (BBus (Finance) LLB)
Licensed Conveyancer
Email: marissa@keyharbor.com.au

Key Harbor
ABN: 48 913 706
Suite 14, Level 3, 9 Calloway Road Lindhurst Park, NSW 2178
Phone: 1300 682 917

Sydney - Melbourne - Brisbane (Perhaps have this along the bottom of the card)

Requirements
Must have
• Sleek, modern and top end appeal (But approachable)
Should not have
• Not too cluttered

```html
<!DOCTYPE html>
<html lang="en">
<head>
<meta charset="utf-8">
<title>Key Harbor – Business Card</title>
<link rel="stylesheet" href="https://fonts.googleapis.com/css2?family=Open+Sans:wght@400;600;700&family=Arimo:wght@400;700&display=swap">
<style>
  :root {
    --backdrop: #2b2a29;
    --card: #070809;
    --card-edge: #141618;
    --brand-grey: #6b6e72;
    --tagline-grey: #55585c;
    --text-grey: #9a9da1;
    --accent-blue: #3f86d6;
    --accent-navy: #2e6aa8;
    --accent-green: #9bd12a;
    --rule-blue: #2a5f8f;
    --rule-grey: #55585c;
  }
  * { box-sizing: border-box; margin: 0; padding: 0; }
  html, body {
    width: 1200px; height: 1200px; overflow: hidden;
    background: var(--backdrop);
  }
  .canvas {
    position: relative; width: 1200px; height: 1200px;
    display: flex; flex-direction: column; align-items: center; justify-content: center; gap: 64px;
  }
  .card {
    position: relative; width: 740px; height: 428px;
    background: var(--card);
    border: 1px solid var(--card-edge);
    box-shadow: 0 10px 30px rgba(0,0,0,.45);
    overflow: hidden;
  }

  /* Back of card */
  .card-back .brand {
    position: absolute; left: 0; right: 0; top: 150px;
    display: flex; align-items: center; justify-content: center; gap: 14px;
  }
  .brand-mark { width: 30px; height: 30px; background: var(--accent-navy); flex: none; }
  .brand-name {
    font-family: "Arimo", sans-serif; font-weight: 700;
    color: var(--brand-grey); font-size: 44px; letter-spacing: -0.5px; white-space: nowrap;
  }
  .tagline {
    position: absolute; left: 0; right: 0; bottom: 80px; text-align: center;
    font-family: "Arimo", sans-serif; font-size: 22px; letter-spacing: 0.5px;
    color: var(--tagline-grey); text-transform: uppercase; white-space: nowrap;
  }

  /* Front of card */
  .card-front .brand {
    position: absolute; left: 60px; top: 160px;
    display: flex; align-items: center; gap: 12px;
  }
  .card-front .brand-name { font-size: 40px; }
  .contact {
    position: absolute; left: 360px; top: 50px; width: 350px;
    font-family: "Open Sans", sans-serif; color: var(--text-grey); font-size: 15px; line-height: 1.45;
  }
  .person-name {
    font-weight: 700; font-size: 21px; color: var(--accent-blue); letter-spacing: 0.5px;
    text-transform: uppercase; white-space: nowrap;
  }
  .person-name .credentials {
    font-weight: 400; font-size: 14px; color: var(--text-grey); text-transform: none; letter-spacing: 0;
  }
  .icon-line { display: flex; align-items: center; gap: 8px; }
  .icon-line svg { flex: none; }
  .divider { border: 0; border-top: 1px solid var(--rule-blue); margin: 12px 0 10px; }
  .company-name { font-weight: 700; color: var(--accent-green); font-size: 15px; }
  .cities {
    position: absolute; left: 0; right: 0; bottom: 36px;
    display: flex; align-items: center; gap: 12px;
    font-family: "Open Sans", sans-serif; font-weight: 700; font-size: 15px; text-transform: uppercase;
  }
  .cities .rule { flex: 1; height: 1px; background: var(--rule-grey); }
  .cities .dot { width: 6px; height: 6px; border-radius: 50%; background: var(--rule-grey); }
  .city-sydney { color: var(--accent-blue); }
  .city-melbourne { color: var(--accent-navy); }
  .city-brisbane { color: var(--accent-green); }
</style>
</head>
<body>
<main class="canvas">
  <section class="card card-back" aria-label="Back of business card">
    <div class="brand">
      <span class="brand-mark"></span>
      <span class="brand-name">KeyHarbor</span>
    </div>
    <p class="tagline">Careful Advice, Dependable Results</p>
  </section>

  <section class="card card-front" aria-label="Front of business card">
    <div class="brand">
      <span class="brand-mark"></span>
      <span class="brand-name">KeyHarbor</span>
    </div>

    <div class="contact">
      <p class="person-name">Marissa Toll <span class="credentials">(BBus (Finance) LLB)</span></p>
      <p>Licensed Conveyancer</p>
      <p class="icon-line">
        <svg width="16" height="16" viewBox="0 0 16 16" aria-hidden="true">
          <circle cx="8" cy="8" r="8" fill="#3f86d6"/>
          <rect x="4" y="5" width="8" height="6" fill="none" stroke="#070809" stroke-width="1.2"/>
          <path d="M4 5 L8 8.5 L12 5" fill="none" stroke="#070809" stroke-width="1.2"/>
        </svg>
        marissa@keyharbor.com.au
      </p>
      <hr class="divider">
      <p class="company-name">Key Harbor</p>
      <p>ABN: 48 913 706</p>
      <p>Suite 14, Level 3</p>
      <p>9 Calloway Road Lindhurst Park, NSW 2178</p>
      <p class="icon-line">
        <svg width="16" height="16" viewBox="0 0 16 16" aria-hidden="true">
          <circle cx="8" cy="8" r="8" fill="#9bd12a"/>
          <path d="M5.2 4.2 L6.8 4 L7.4 6 L6.4 6.8 Q7.2 8.6 9.2 9.6 L10 8.6 L12 9.2 L11.8 10.8 Q8 11.4 5.2 4.2 Z" fill="#070809"/>
        </svg>
        1300 682 917
      </p>
    </div>

    <div class="cities">
      <span class="rule"></span>
      <span class="city-sydney">Sydney</span>
      <span class="dot"></span>
      <span class="city-melbourne">Melbourne</span>
      <span class="dot"></span>
      <span class="city-brisbane">Brisbane</span>
      <span class="rule"></span>
    </div>
  </section>
</main>
</body>
</html>
```